Ravel Oversight Partners - Statonery Design

I just completed a redesign of my business card. Please do not design a logo or business card. See my current stationery design attached.

Target Market(s)

VP of Human Resources and Finance - Companies with 100 employees to 10,000

Industry/Entity Type

Business Consultant

Requirements
Must have
• Use the letterhead instructions for the color and fonts.

```html
<!DOCTYPE html>
<html lang="en">
<head>
<meta charset="utf-8">
<title>Ravel Oversight Partners – Stationery</title>
<link rel="stylesheet" href="https://fonts.googleapis.com/css2?family=Catamaran:wght@400;500;600;700&display=swap">
<style>
  :root {
    --plum: #6a1f45;
    --plum-faint: #e2d3dc;
    --paper: #ffffff;
    --backdrop: #efefee;
    --ink: #4a4a4a;
    --ink-soft: #6b6b6b;
    --label: #1d3a5c;
    --sig-tone: #d9d4d7;
  }
  * { box-sizing: border-box; margin: 0; padding: 0; }
  html, body { width: 1035px; height: 1200px; overflow: hidden; }
  body {
    position: relative;
    background: var(--backdrop);
    font-family: "Catamaran", sans-serif;
    color: var(--ink);
  }
  .piece { position: absolute; background: var(--paper); overflow: hidden; }

  /* Business cards */
  .card { width: 178px; height: 101px; top: 96px; background: var(--plum);
          display: flex; align-items: center; justify-content: center; gap: 8px; }
  .card--one { left: 98px; }
  .card--two { left: 306px; }
  .card__dot { width: 30px; height: 30px; border-radius: 50%; background: var(--paper); flex: none; }
  .card__name { color: var(--paper); font-size: 10px; font-weight: 600; line-height: 1.2; }

  /* Brand mark replacement */
  .brand { position: absolute; display: flex; align-items: center; gap: 6px; }
  .brand__dot { width: 36px; height: 36px; border-radius: 50%; background: var(--plum); flex: none; }
  .brand__name { color: var(--plum); font-size: 10px; font-weight: 600; line-height: 1.15; }

  /* Letterhead header */
  .contact { position: absolute; font-size: 5.6px; line-height: 10px; color: var(--ink-soft); }
  .contact__firm { color: var(--plum); font-weight: 700; }
  .contact--lines { padding-left: 7px; border-left: 0.8px solid var(--plum); }
  .contact__row { display: flex; align-items: center; gap: 4px; }
  .contact__row svg { width: 5px; height: 5px; fill: var(--plum); flex: none; }

  .sheet { width: 365px; height: 516px; top: 248px; }
  .sheet--blank { left: 106px; }
  .sheet--letter { left: 544px; width: 400px; }

  .sheet__decor { position: absolute; left: 262px; top: 405px; width: 104px; height: 104px;
                  border-radius: 50%; background: var(--plum-faint); }
  .sheet__decor-name { position: absolute; right: 110px; bottom: 14px; font-size: 9px;
                       font-weight: 600; color: var(--plum-faint); }

  /* Letter body */
  .letter__to { position: absolute; left: 26px; top: 176px; font-size: 7.6px; line-height: 12.5px; }
  .letter__to-name { color: var(--plum); font-weight: 700; font-size: 8.4px; }
  .letter__date { position: absolute; right: 25px; top: 176px; font-size: 7.6px; }
  .letter__body { position: absolute; left: 26px; top: 244px; width: 349px;
                  font-size: 7.4px; line-height: 13.6px; text-align: justify; }
  .letter__body p + p { margin-top: 13.6px; }
  .letter__close { position: absolute; left: 26px; top: 398px; font-size: 6px; }
  .letter__signature { position: absolute; left: 26px; top: 410px; width: 56px; height: 18px;
                       background: var(--sig-tone); }
  .letter__signer { position: absolute; left: 26px; top: 434px; font-size: 6.4px; color: var(--ink-soft); }

  /* Labels */
  .label { position: absolute; width: 420px; text-align: center; font-size: 17px;
           font-weight: 500; color: var(--label); }

  /* Envelopes */
  .envelope { width: 449px; height: 200px; top: 891px; }
  .envelope--front { left: 50px; }
  .envelope--back { left: 526px; }
  .envelope__return { position: absolute; left: 27px; top: 140px; padding-left: 9px;
                      border-left: 1px solid var(--plum); font-size: 7.6px; line-height: 12px; color: var(--ink-soft); }
  .envelope__return .contact__firm { font-size: 7.6px; }
  .envelope__flap { position: absolute; left: 0; top: 0; width: 449px; height: 72px; }
</style>
</head>
<body>

  <!-- Business cards -->
  <div class="piece card card--one">
    <span class="card__dot"></span>
    <span class="card__name">Ravel Oversight<br>Partners</span>
  </div>
  <div class="piece card card--two">
    <span class="card__dot"></span>
    <span class="card__name">Ravel Oversight<br>Partners</span>
  </div>

  <!-- Letterhead, blank -->
  <section class="piece sheet sheet--blank">
    <div class="brand" style="left:23px; top:34px;">
      <span class="brand__dot"></span>
      <span class="brand__name">Ravel Oversight<br>Partners</span>
    </div>
    <div class="contact" style="left:149px; top:37px;">
      <div class="contact__firm">RAVELOVERSIGHT</div>
      <div>118 Larkspur Avenue NW</div>
      <div>Suite 40 Gran Harbor, MI 49021</div>
    </div>
    <div class="contact contact--lines" style="left:236px; top:37px;">
      <div class="contact__row"><svg viewBox="0 0 10 10"><path d="M2 0l2 2-1 2 3 3 2-1 2 2-2 2C4 10 0 6 0 2z"/></svg>555. 014. 2287</div>
      <div class="contact__row"><svg viewBox="0 0 10 10"><path d="M0 2h10v6H0zM0 2l5 3 5-3" stroke="#fff" stroke-width="0.8"/></svg>jdaley@raveloversight.com</div>
      <div class="contact__row"><svg viewBox="0 0 10 10"><circle cx="5" cy="5" r="5"/></svg>www.raveloversight.com</div>
    </div>
    <div class="sheet__decor"></div>
    <div class="sheet__decor-name">Ravel Oversight Partners</div>
  </section>

  <!-- Letterhead, word document -->
  <section class="piece sheet sheet--letter">
    <div class="brand" style="left:28px; top:34px;">
      <span class="brand__dot"></span>
      <span class="brand__name">Ravel Oversight<br>Partners</span>
    </div>
    <div class="contact" style="left:164px; top:37px;">
      <div class="contact__firm">RAVELOVERSIGHT</div>
      <div>118 Larkspur Avenue NW</div>
      <div>Suite 40 Gran Harbor, MI 49021</div>
    </div>
    <div class="contact contact--lines" style="left:259px; top:37px;">
      <div class="contact__row"><svg viewBox="0 0 10 10"><path d="M2 0l2 2-1 2 3 3 2-1 2 2-2 2C4 10 0 6 0 2z"/></svg>555. 014. 2287</div>
      <div class="contact__row"><svg viewBox="0 0 10 10"><path d="M0 2h10v6H0zM0 2l5 3 5-3" stroke="#fff" stroke-width="0.8"/></svg>jdaley@raveloversight.com</div>
      <div class="contact__row"><svg viewBox="0 0 10 10"><circle cx="5" cy="5" r="5"/></svg>www.raveloversight.com</div>
    </div>

    <div class="letter__to">
      <div class="letter__to-name">Dana Whitlock</div>
      <div>Manager</div>
      <div>48 Orchard Lane</div>
      <div>Millbrook, NC</div>
    </div>
    <div class="letter__date">Date: 23/02/2019</div>

    <div class="letter__body">
      <p>Lorem ipsum dolor sit amet, consectetuer adipiscing elit, sed diam nonummy nibh euismod tincidunt ut laoreet dolore magna aliquam erat volutpat. Ut wisi enim ad minim veniam, quis nostrud exerci tation ullamcorper suscipit lobortis nisl ut aliquip ex ea commodo consequat. Lorem ipsum dolor sit amet, cons ectetuer adipiscing elit, sed diam nonummy nibh euismod tincidunt ut laoreet dolore magna aliquam erat volutpat. Ut wisi enim ad minim veniam, quis nostrud exerci tation ullamcorper suscipit lobortis nisl ut aliquip ex ea commodo consequat. Lorem ipsum dolor sit amet, consectetuer adipiscing elit, sed diam nonummy nibh euismod tincidunt ut laoreet dolore magna aliquam erat volutpat. Ut wisi enim ad minim veniam,</p>
      <p>consequat. Duis autem vel eum iriure dolor in hendrerit in vulputate velit esse molestie consequat, vel illum dolore eu feugiat nulla facilisis at vero eros et accumsan .</p>
    </div>
    <div class="letter__close">sincerely</div>
    <div class="letter__signature" role="img" aria-label="Handwritten signature"></div>
    <div class="letter__signer">Owen Hartley</div>
  </section>

  <!-- Labels -->
  <div class="label" style="left:56px; top:795px;">Letterhead</div>
  <div class="label" style="left:558px; top:795px;">Word Document Letterhead</div>
  <div class="label" style="left:51px; top:843px;">Envelope</div>
  <div class="label" style="left:558px; top:843px;">Envelope</div>

  <!-- Envelope, front -->
  <section class="piece envelope envelope--front">
    <div class="brand" style="left:27px; top:28px;">
      <span class="brand__dot" style="width:42px; height:42px;"></span>
      <span class="brand__name" style="font-size:11.5px;">Ravel Oversight<br>Partners</span>
    </div>
    <div class="envelope__return">
      <div class="contact__firm">RAVELOVERSIGHT</div>
      <div>118 Larkspur Avenue NW</div>
      <div>Suite 40 Gran Harbor, MI 49021</div>
    </div>
  </section>

  <!-- Envelope, back -->
  <section class="piece envelope envelope--back">
    <svg class="envelope__flap" viewBox="0 0 449 72" aria-hidden="true">
      <polygon points="0,0 449,0 438,72 11,72" fill="var(--plum)"/>
      <circle cx="224" cy="36" r="24" fill="var(--paper)"/>
    </svg>
    <div style="position:absolute; left:0; top:80px; width:449px; text-align:center; font-size:9px; font-weight:600; color:var(--plum);">Ravel Oversight Partners</div>
  </section>

</body>
</html>
```